Redesign our current website with a more professional feel

We currently have a running website that generates some traffic and looks ok but now we want to revamp it with professional eye catching design.
We are open to proposals and open to any new ideas or suggestions but we have to see your previous work.
our current site is www.brelk-solutions.com.au

Thank you for your time and we look forward to seeing your proposals

Target Market(s)

Business owners, managers

Industry/Entity Type

Security

Number of Pages Required

5+ page

```html
<!DOCTYPE html>
<html lang="en">
<head>
<meta charset="utf-8">
<title>Brelk Solutions – Quality Security Service</title>
<link href="https://fonts.googleapis.com/css2?family=Raleway:wght@300;400;500&family=Open+Sans:wght@400;600&display=swap" rel="stylesheet">
<style>
:root{
  --navy:#0c1536;
  --navy-deep:#060b20;
  --band:#1e4282;
  --sky:#5aa6ef;
  --sky-light:#64a9ee;
  --white:#ffffff;
  --card:#ececec;
  --ink:#666a70;
  --name:#1e3a78;
}
*{margin:0;padding:0;box-sizing:border-box}
html,body{width:777px;height:1200px;overflow:hidden}
body{position:relative;font-family:"Open Sans",sans-serif;color:var(--white);background:var(--navy)}
.hero{position:absolute;left:0;top:0;width:777px;height:616px;
  background:radial-gradient(ellipse at 20% 25%,#3a2a22 0%,transparent 45%),
             radial-gradient(ellipse at 80% 85%,#2a2f4a 0%,transparent 50%),
             linear-gradient(180deg,#0b1333 0%,#101a3e 60%,#1a2038 100%)}
.logo-plate{position:absolute;left:30px;top:0;width:158px;height:76px}
.logo-name{position:absolute;left:62px;top:18px;font-family:"Raleway",sans-serif;font-weight:500;font-size:20px;color:var(--name);letter-spacing:1px;display:flex;align-items:center;gap:6px}
.logo-name .dot{width:10px;height:10px;border-radius:50%;background:var(--name)}
.nav{position:absolute;top:21px;left:270px;display:flex;gap:29px;font-size:7.5px;font-weight:600;letter-spacing:.2px}
.nav a{color:var(--white);text-decoration:none}
.nav a.active{color:var(--sky)}
.call{position:absolute;left:656px;top:14px;display:flex;align-items:center;gap:6px}
.call-label{font-size:7px;color:var(--sky);line-height:1.1}
.call-number{font-size:9.5px;color:var(--white);font-weight:600}
.header-rule{position:absolute;left:0;top:53px;width:777px;height:1px;background:rgba(255,255,255,.35)}
.hero-title{position:absolute;top:194px;width:777px;text-align:center;font-family:"Raleway",sans-serif;font-weight:300;font-size:37px;line-height:44px;letter-spacing:.5px}
.hero-title .accent{color:var(--sky)}
.connector{position:absolute;left:160px;top:441px;width:440px;height:1px;background:var(--white)}
.feature{position:absolute;top:401px;width:180px;text-align:center}
.feature .icon{width:80px;height:80px;border-radius:50%;margin:0 auto;display:flex;align-items:center;justify-content:center;background:var(--sky)}
.feature .icon.light{background:var(--white)}
.feature h3{font-family:"Raleway",sans-serif;font-weight:400;font-size:12px;color:var(--sky);margin-top:14px}
.feature p{font-size:7.4px;line-height:10.5px;margin-top:7px}
.feature .more{display:inline-block;font-size:7.4px;margin-top:6px;color:var(--sky)}
.feature .more.plain{color:var(--white)}
.about{position:absolute;left:0;top:616px;width:777px;height:227px;background:var(--band);text-align:center}
.about h2{font-family:"Raleway",sans-serif;font-weight:400;font-size:19px;margin-top:30px}
.about p{font-size:8.4px;line-height:14.6px;width:620px;margin:13px auto 0}
.about .btn{display:inline-block;margin-top:15px;width:87px;height:23px;line-height:23px;background:var(--white);color:#333;font-size:7px}
.testimonials{position:absolute;left:0;top:843px;width:777px;height:275px;
  background:linear-gradient(180deg,#1c2436 0%,#2a2a33 55%,#3a2e26 100%)}
.testimonials h2{position:absolute;top:27px;width:777px;text-align:center;font-family:"Raleway",sans-serif;font-weight:500;font-size:22px}
.testimonials h2 span{color:var(--sky)}
.quote{position:absolute;font-family:Georgia,serif;font-size:30px;color:var(--sky);font-style:italic}
.card{position:absolute;left:80px;top:93px;width:596px;height:98px;background:var(--card)}
.avatar{position:absolute;left:24px;top:16px;width:70px;height:70px;border-radius:50%;border:2px solid #fff;background:linear-gradient(180deg,#c9b6a5,#3a3f4a)}
.card p{position:absolute;left:112px;top:17px;width:450px;font-size:9.3px;line-height:13px;color:var(--ink)}
.card .author{position:absolute;right:40px;top:72px;font-size:10px;font-weight:600;color:var(--name)}
.dots{position:absolute;top:229px;left:372px;display:flex;gap:4px}
.dots i{width:8px;height:8px;border-radius:50%;border:1px solid var(--sky)}
.dots i.on{background:var(--sky)}
.footer{position:absolute;left:0;top:1118px;width:777px;height:82px;background:var(--sky-light);text-align:center}
.footer .links{margin-top:29px;font-size:7.5px}
.footer .copy{margin-top:6px;font-size:6.3px}
.social{position:absolute;right:43px;top:38px;display:flex;gap:16px}
.social i{width:9px;height:9px;border-radius:50%;background:rgba(255,255,255,.6)}
</style>
</head>
<body>
<section class="hero" role="img" aria-label="Night city photo with light trails and harbour bridge">
</section>

<svg class="logo-plate" viewBox="0 0 158 76"><polygon points="0,0 156,0 152,62 6,76" fill="#ececec"/></svg>
<div class="logo-name"><span class="dot"></span>BRELK</div>

<nav class="nav">
  <a class="active" href="#">HOME</a><a href="#">ABOUT US</a><a href="#">SERVICES</a><a href="#">CONTACT US</a><a href="#">SPECIAL OFFERS</a>
</nav>
<div class="call">
  <svg width="26" height="26" viewBox="0 0 26 26"><circle cx="13" cy="13" r="12" fill="none" stroke="#5aa6ef"/><path d="M9 8c-1 1-1 3 1 6s4 4 6 4l1-2-2-2-1 1c-1 0-3-2-3-3l1-1-2-2z" fill="#5aa6ef"/></svg>
  <div><div class="call-label">CALL US</div><div class="call-number">(123) 456-7890</div></div>
</div>
<div class="header-rule"></div>

<h1 class="hero-title">QUALITY SECURITY SERVICE BY<br><span class="accent">SECURITY COMPANY SYDNEY</span></h1>

<div class="connector"></div>
<div class="feature" style="left:71px">
  <div class="icon light"><svg width="30" height="30" viewBox="0 0 30 30"><circle cx="15" cy="15" r="12" fill="none" stroke="#5aa6ef" stroke-width="6"/><circle cx="15" cy="15" r="5" fill="#fff"/></svg></div>
  <h3>Services</h3>
  <p>Lorem ipsum dolor sit amet, consectetur edit adipiscing elit, sed do eiusmod tempor incididunt utdolore magna aliqua.</p>
  <span class="more plain">Read More ▸</span>
</div>
<div class="feature" style="left:295px">
  <div class="icon"><svg width="32" height="32" viewBox="0 0 32 32"><path d="M3 30V4h12a6 6 0 0 1 6 6v12h-5V10h-7v20zM12 14h5v14h7V2h5v20a8 8 0 0 1-8 8h-9z" fill="#fff"/></svg></div>
  <h3>Special Offers</h3>
  <p>Lorem ipsum dolor sit amet, consectetur edit adipiscing elit, sed do eiusmod tempor incididunt utdolore magna aliqua.</p>
  <span class="more">Read More ▸</span>
</div>
<div class="feature" style="left:510px">
  <div class="icon"><svg width="28" height="36" viewBox="0 0 28 36"><rect x="0" y="0" width="28" height="36" fill="#fff"/><g fill="#5aa6ef"><rect x="5" y="5" width="3" height="3"/><rect x="11" y="5" width="3" height="3"/><rect x="17" y="5" width="3" height="3"/><rect x="5" y="11" width="3" height="3"/><rect x="11" y="11" width="3" height="3"/><rect x="17" y="11" width="3" height="3"/><rect x="5" y="17" width="3" height="3"/><rect x="11" y="17" width="3" height="3"/><rect x="17" y="17" width="3" height="3"/><rect x="10" y="27" width="8" height="6"/></g></svg></div>
  <h3>Latest News</h3>
  <p>Lorem ipsum dolor sit amet, consectetur edit adipiscing elit, sed do eiusmod tempor incididunt utdolore a aliqua.</p>
  <span class="more">Read More ▸</span>
</div>

<section class="about">
  <h2>Quality Security Service By Security Company Sydney</h2>
  <p>Lorem ipsum dolor sit amet, consectetur adipiscing elit, sed do eiusmod tempor incididunt ut labore et dolore magna aliqua. Ut enim ad minim veniam, quis nostrud exercitation ullamco laboris nisi ut aliquip ex ea commodo consequat.</p>
  <p>Lorem ipsum dolor sit amet, consectetur adipiscing elit, sed do eiusmod tempor incididunt ut labore et dolore magna aliqua. Ut enim ad minim veniam, quis nostrud exercitation ullamco laboris nisi ut aliquip ex ea commodo consequat. Duis aute irure dolor in reprehenderit in voluptate velit esse cillum dolore eu fugiat nulla pariatur. Excepteur sint occaecat cupidatat non proident, sunt in culpa qui officia deserunt mollit anim id est laborum.</p>
  <span class="btn">READMORE</span>
</section>

<section class="testimonials" role="img" aria-label="Harbour city skyline at night with opera house">
  <h2>Our <span>Testimonials</span></h2>
  <span class="quote" style="left:82px;top:60px">“</span>
  <span class="quote" style="left:658px;top:200px">”</span>
  <div class="card">
    <div class="avatar" role="img" aria-label="Client portrait"></div>
    <p>Lorem ipsum dolor sit amet, consectetur adipiscing elit, sed do eiusmod tempor incididunt ut labore et dolore magna aliqua. Ut enim ad minim veniam, quis nostrud exercitation ullamco laboris nisi ut aliquip ex ea commodo consequat.</p>
    <span class="author">- Adam Corrin</span>
  </div>
  <div class="dots"><i></i><i class="on"></i><i></i></div>
</section>

<footer class="footer">
  <div class="links">Home &nbsp;/ About us &nbsp;/ Service Us &nbsp;/ Contact Us</div>
  <div class="copy">© All Rights Reserved. Copyrights @CompanyName .2016</div>
  <div class="social"><i></i><i></i><i></i><i></i><i></i></div>
</footer>
</body>
</html>
```